Tamarind Lodgings letterhead

We need a letterhead designed that includes the new logo that has just been designed for our business. The letterhead will need to be formatted for digital use as well as for print.

Target Market(s)

Private tenant, corporate tenants, real estate agents

Industry/Entity Type

Digital

Requirements
Must have
• ABN 58 907 412 336
PO Box 8163, Coral Bend Mail Centre QLD 4762
Email: marlow.pike@inboxnest.com
Ph: 0437 592 064

```html
<!DOCTYPE html>
<html lang="en">
<head>
<meta charset="utf-8">
<title>Tamarind Lodgings Letterhead</title>
<link rel="stylesheet" href="https://fonts.googleapis.com/css2?family=Open+Sans:wght@400;700&display=swap">
<style>
  :root {
    --backdrop: #cfe3ea;
    --paper: #ffffff;
    --maroon: #5c0a24;
    --maroon-tint: #e9d6dc;
    --ink: #2b2b2b;
    --muted: #555555;
  }
  * { margin: 0; padding: 0; box-sizing: border-box; }
  html, body { width: 1200px; height: 1101px; overflow: hidden; }
  body {
    background: var(--backdrop);
    font-family: "Open Sans", Arial, sans-serif;
    color: var(--ink);
    position: relative;
  }
  .letterhead {
    position: absolute;
    left: 239px;
    top: 40px;
    width: 722px;
    height: 1021px;
    background: var(--paper);
    overflow: hidden;
    box-shadow: 0 2px 10px rgba(0,0,0,0.12);
  }
  .edge-bar {
    position: absolute;
    top: 34px;
    height: 88px;
    background: var(--maroon);
  }
  .edge-bar--outer { left: 4px; width: 11px; }
  .edge-bar--inner { left: 21px; width: 12px; }
  .brand {
    position: absolute;
    right: 44px;
    top: 38px;
    display: flex;
    align-items: center;
    gap: 12px;
  }
  .brand__square {
    width: 70px;
    height: 70px;
    background: var(--maroon);
    border-radius: 8px;
  }
  .brand__name {
    font-weight: 700;
    color: var(--maroon);
    font-size: 26px;
    line-height: 1.05;
    text-transform: uppercase;
    letter-spacing: 0.5px;
  }
  .letter {
    position: absolute;
    left: 49px;
    top: 222px;
    width: 612px;
    font-size: 13.6px;
    line-height: 21.7px;
  }
  .letter p { margin-bottom: 22px; text-align: justify; }
  .letter .greeting { margin-bottom: 24px; }
  .letter .closing { margin-bottom: 20px; }
  .signature {
    position: absolute;
    left: 49px;
    top: 748px;
    width: 120px;
    height: 36px;
    background: linear-gradient(90deg, #f1f1f1, #e6e6e6);
    border-radius: 4px;
  }
  .signatory {
    position: absolute;
    left: 49px;
    top: 790px;
    font-size: 8.5px;
    color: var(--ink);
  }
  .contact {
    position: absolute;
    left: 49px;
    top: 866px;
    font-size: 12.5px;
    line-height: 15.5px;
    color: var(--muted);
    font-style: normal;
  }
  .corner-decoration {
    position: absolute;
    right: 0;
    bottom: 0;
    width: 260px;
    height: 150px;
    background: linear-gradient(160deg, var(--paper) 30%, var(--maroon-tint));
  }
</style>
</head>
<body>
  <main class="letterhead">
    <div class="edge-bar edge-bar--outer"></div>
    <div class="edge-bar edge-bar--inner"></div>

    <header class="brand">
      <div class="brand__square"></div>
      <div class="brand__name">Tamarind<br>Lodgings</div>
    </header>

    <section class="letter">
      <p class="greeting">Dear Folks</p>
      <p>Lorem ipsum dolor sit amet, consectetur adipiscing elit. Quisque dictum leo quis mauris dictum auctor. Praesent viverra, elit at rutrum fringilla, purus nisi feugiat est, sit amet lobortis magna mauris id nibh. Sed interdum massa non mauris faucibus cursus. Integer at tellus sit amet lacus ultrices ullamcorper. Nunc vel libero dui, sit amet pellentesque ligula. Suspendisse semper, urna.</p>
      <p>Aenean quis nisi arcu, blandit mollis odio. Vestibulum nulla enim, viverra a auctor quis, suscipit rhoncus libero. Donec quis libero vel magna luctus pulvinar. Duis eget nulla vel massa commodo semper placerat id leo. Nunc eu leo sed quam hendrerit accumsan. Maecenas eleifend nisi non velit dignissim ut suscipit arcu imperdiet. Phasellus nisi nulla, tincidunt. Proin tincidunt, est sed rhoncus mattis, nunc sem aliquet quam, eget tristique augue dolor vel orci. Vestibulum et tellus dui, vitae sollicitudin sapien. Pellentesque nisl tortor, faucibus in mollis non, dignissim et felis.</p>
      <p>Phasellus nisi nulla, tincidunt. Proin tincidunt, est sed rhoncus mattis, nunc sem aliquet quam, eget tristique augue dolor vel orci. Vestibulum et tellus dui, vitae sollicitudin sapien. Pellentesque nisl tortor, faucibus in mollis non, dignissim et felis.</p>
      <p class="closing">Sincerely,</p>
      <p>Good Looking</p>
    </section>

    <div class="signature" role="img" aria-label="Handwritten signature of Nora Vale"></div>
    <p class="signatory">Nora Vale, Co-Founder &amp; CEO</p>

    <address class="contact">
      ABN 58 907 412 336<br>
      PO Box 8163,<br>
      Coral Bend Mail Centre QLD 4762<br>
      Email: marlow.pike@inboxnest.com<br>
      Ph: 0437 592 064
    </address>

    <div class="corner-decoration" role="img" aria-label="Decorative corner area in soft maroon tones"></div>
  </main>
</body>
</html>
```